Brindle Logistics Business Card Design

We are a trucking and warehousing company. We run freight in the US manly from the Pacific NW to TX and back up the the PNW. We also do warehousing where we store, move, and distribute freight. Looking for a clean and modern design of business card. We would like to look rich and elegant. Attached is our logo.

Industry/Entity Type

Trucking Company

Contact Information for Business Card

Looking for a clean and modern design of business card. We would like to look rich and elegant.

Font styles to use
Sans Serif

Colors

Designer to choose colors to be used in the design.

Requirements
Must have
• logo but it should not dominate the card
Should not have
• logo should not dominate the card

```html
<!DOCTYPE html>
<html lang="en">
<head>
<meta charset="utf-8">
<title>Brindle Logistics – Business Card</title>
<link rel="stylesheet" href="https://fonts.googleapis.com/css2?family=Arimo:wght@400;700&display=swap">
<style>
  :root {
    --stage: #e9eaec;
    --card-white: #f7f7f5;
    --brand-blue: #0b6ab5;
    --brand-orange: #ef9420;
    --charcoal: #333338;
    --text-light: #ffffff;
    --shadow: 0 14px 30px rgba(0,0,0,0.22);
  }
  * { box-sizing: border-box; margin: 0; padding: 0; }
  html, body {
    width: 1200px; height: 800px; overflow: hidden;
    background: var(--stage);
    font-family: "Arimo", Arial, sans-serif;
  }
  .stage { position: relative; width: 1200px; height: 800px; }
  .card {
    position: absolute; width: 520px; height: 300px;
    border-radius: 4px; overflow: hidden;
    box-shadow: var(--shadow);
  }
  .card-front { left: 200px; top: 60px; background: var(--card-white); }
  .card-back  { left: 480px; top: 430px; background: var(--brand-blue); }

  .swoosh { position: absolute; inset: 0; width: 100%; height: 100%; }

  .wordmark {
    position: absolute; display: flex; align-items: center; gap: 12px;
    font-weight: 700; letter-spacing: 0.06em; text-transform: uppercase;
  }
  .wordmark-dot { width: 34px; height: 34px; border-radius: 50%; background: currentColor; flex: none; }
  .wordmark-name { display: flex; flex-direction: column; line-height: 1; }
  .wordmark-name .primary { font-size: 40px; }
  .wordmark-name .secondary { font-size: 16px; letter-spacing: 0.1em; margin-top: 4px; }

  .card-front .wordmark { left: 122px; top: 82px; color: var(--brand-blue); }
  .card-back .wordmark { right: 36px; top: 34px; color: var(--text-light); }
  .card-back .wordmark-name .primary { font-size: 34px; }
  .card-back .wordmark-name .secondary { font-size: 14px; }

  .emblem-area {
    position: absolute; left: 0; top: 0; width: 235px; height: 300px;
    background: linear-gradient(90deg, var(--card-white) 70%, #dfe9f3 100%);
    border-radius: 0 140px 0 0;
  }

  .contact-list {
    position: absolute; right: 36px; top: 132px;
    list-style: none; color: var(--text-light);
    font-size: 14px; text-align: right;
  }
  .contact-list li {
    display: flex; justify-content: flex-end; align-items: center;
    gap: 12px; height: 30px;
  }
  .contact-icon { width: 15px; height: 15px; fill: none; stroke: var(--text-light); stroke-width: 2; flex: none; }
</style>
</head>
<body>
<main class="stage">

  <section class="card card-front" aria-label="Business card front">
    <svg class="swoosh" viewBox="0 0 520 300" preserveAspectRatio="none" aria-hidden="true">
      <path d="M300,240 Q460,195 520,90 L520,150 Q470,225 330,248 Z" fill="var(--charcoal)"/>
      <path d="M0,185 C150,250 380,270 520,140 L520,300 L0,300 Z" fill="var(--brand-blue)"/>
      <path d="M0,180 C150,245 380,262 505,150" fill="none" stroke="var(--brand-orange)" stroke-width="9" stroke-linecap="round"/>
      <path d="M40,232 C200,256 300,252 390,242" fill="none" stroke="var(--charcoal)" stroke-width="3" stroke-linecap="round"/>
    </svg>
    <div class="wordmark">
      <span class="wordmark-dot"></span>
      <span class="wordmark-name">
        <span class="primary">Brindle</span>
        <span class="secondary">Logistics, LLC</span>
      </span>
    </div>
  </section>

  <section class="card card-back" aria-label="Business card back">
    <div class="emblem-area" role="img" aria-label="Large bird-head emblem illustration in blue, white and orange"></div>

    <div class="wordmark">
      <span class="wordmark-name">
        <span class="primary">Brindle</span>
        <span class="secondary">Logistics, LLC</span>
      </span>
    </div>

    <ul class="contact-list">
      <li>Your contact no. here
        <svg class="contact-icon" viewBox="0 0 24 24" aria-hidden="true"><path d="M5 3h4l2 5-3 2a11 11 0 0 0 6 6l2-3 5 2v4a2 2 0 0 1-2 2A17 17 0 0 1 3 5a2 2 0 0 1 2-2z"/></svg>
      </li>
      <li>yourmailid@mailbox.com
        <svg class="contact-icon" viewBox="0 0 24 24" aria-hidden="true"><rect x="3" y="5" width="18" height="14" rx="1"/><path d="M3 6l9 7 9-7"/></svg>
      </li>
      <li>www.yourwebaddress.com
        <svg class="contact-icon" viewBox="0 0 24 24" aria-hidden="true"><circle cx="12" cy="12" r="9"/><path d="M3 12h18M12 3c3 3 3 15 0 18M12 3c-3 3-3 15 0 18"/></svg>
      </li>
      <li>Your address here
        <svg class="contact-icon" viewBox="0 0 24 24" aria-hidden="true"><path d="M12 22s7-7 7-12a7 7 0 0 0-14 0c0 5 7 12 7 12z"/><circle cx="12" cy="10" r="2.5"/></svg>
      </li>
    </ul>
  </section>

</main>
</body>
</html>
```